Pelton|Marsh & Quillan business card contest

We need a logo for an upscale boutique diversified company involved in real estate, investments, cattle, and more. Our businesses DO NOT need to be reflected in the business card nor do we want them noted. This is our logo and colors and we love our logo and colors. Our logo looks best against a black background and we like to include the firm name in our logo usage. importantly, the names Pelton and Marsh are separated by | not / and we use an ampersand not the word and.
On the front of the card, we want to include:
company logo and name (Pelton|Marsh & Quillan)
on the back, we would definitely include:
address, email, cell #
logo and name (smaller size than front)

The variable will be location of individual name and title (mine for example is ) - whether on the front OR on the back. interested in variations from which to choose
Dr. Neil R. Whitcombe, CFA
Scientifique des Fusées Financières

we would like to use contemporary symbols for address, email address, cell # with an option for web site that we do not intend to use initially. we like two sided cards and believe this design should use four rounded corners with the standard size. we prefer thicker card stock and may look at metal.

```html
<!DOCTYPE html>
<html lang="en">
<head>
<meta charset="utf-8">
<title>Pelton|Marsh &amp; Quillan — Business Card</title>
<link href="https://fonts.googleapis.com/css2?family=Lato:wght@400;700&display=swap" rel="stylesheet">
<style>
  :root {
    --backdrop: #2b2b2c;
    --card: #1d1e20;
    --card-edge: #262729;
    --pattern-a: #232426;
    --pattern-b: #2e2f31;
    --orange: #f08a1c;
    --grey-mark: #8a8a8a;
    --grey-text: #9c9c9c;
    --light-text: #e4e4e4;
    --rule: #6d6d6d;
  }
  * { margin: 0; padding: 0; box-sizing: border-box; }
  html, body {
    width: 1200px; height: 1108px; overflow: hidden;
    background: var(--backdrop);
    font-family: "Lato", Arial, sans-serif;
  }
  .stage {
    position: relative; width: 1200px; height: 1108px;
    display: flex; justify-content: center; align-items: center; gap: 60px;
  }
  .card {
    width: 420px; height: 700px;
    border-radius: 26px;
    background: var(--card);
    border: 1px solid var(--card-edge);
    position: relative; overflow: hidden;
  }
  .card-front {
    display: flex; flex-direction: column; align-items: center;
    padding-top: 120px; text-align: center;
  }
  .brand { display: flex; flex-direction: column; align-items: center; gap: 22px; }
  .brand-square { width: 48px; height: 48px; background: var(--orange); }
  .brand-name { font-size: 30px; font-weight: 400; color: var(--grey-mark); letter-spacing: 0.5px; }
  .person { margin-top: 120px; }
  .person-name {
    font-size: 22px; font-weight: 700; color: var(--orange);
    text-transform: uppercase; letter-spacing: 0.3px;
  }
  .person-title { margin-top: 6px; font-size: 17px; color: var(--grey-text); }
  .icon-rule {
    margin-top: 26px; width: 320px;
    display: flex; align-items: center; gap: 8px;
  }
  .icon-rule .line { flex: 1; height: 1px; background: var(--rule); }
  .icon-rule svg { width: 26px; height: 26px; display: block; }
  .contact { margin-top: 14px; font-size: 18px; line-height: 28px; color: var(--light-text); }
  .address-rule { width: 320px; height: 1px; background: var(--rule); margin-top: 12px; }
  .address { margin-top: 14px; font-size: 18px; line-height: 28px; color: var(--light-text); }
  .card-back .pattern {
    position: absolute; inset: 0;
    background: linear-gradient(160deg, var(--pattern-b) 0%, var(--pattern-a) 55%, var(--card) 100%);
  }
  .back-brand {
    position: absolute; left: 0; right: 0; top: 430px;
    display: flex; align-items: center; justify-content: center; gap: 10px;
  }
  .back-brand .brand-square { width: 22px; height: 22px; }
  .back-brand .brand-name { font-size: 16px; }
</style>
</head>
<body>
<main class="stage">
  <section class="card card-front">
    <div class="brand">
      <div class="brand-square"></div>
      <div class="brand-name">Pelton|Marsh &amp; Quillan</div>
    </div>
    <div class="person">
      <div class="person-name">Dr. Neil R. Whitcombe, CFA</div>
      <div class="person-title">Scientifique des Fusées Financières</div>
    </div>
    <div class="icon-rule">
      <span class="line"></span>
      <svg viewBox="0 0 26 26" aria-label="Phone"><circle cx="13" cy="13" r="13" fill="var(--orange)"/><path d="M9 7.5c.8-.6 1.6-.4 2 .4l1 2c.3.6.1 1.1-.4 1.5l-.6.5c.6 1.4 1.7 2.5 3.1 3.1l.5-.6c.4-.5 1-.7 1.5-.4l2 1c.8.4 1 1.2.4 2-1 1.3-2.4 1.6-4 .8-2.6-1.2-4.6-3.2-5.8-5.8-.8-1.6-.5-3 .3-4.5z" fill="#1d1e20"/></svg>
      <svg viewBox="0 0 26 26" aria-label="Email"><circle cx="13" cy="13" r="13" fill="var(--orange)"/><rect x="6.5" y="8.5" width="13" height="9" fill="#1d1e20"/><path d="M6.5 8.5l6.5 5 6.5-5" fill="none" stroke="var(--orange)" stroke-width="1.2"/></svg>
      <svg viewBox="0 0 26 26" aria-label="Website"><circle cx="13" cy="13" r="13" fill="var(--orange)"/><circle cx="13" cy="13" r="6.5" fill="none" stroke="#1d1e20" stroke-width="1.5"/><ellipse cx="13" cy="13" rx="2.8" ry="6.5" fill="none" stroke="#1d1e20" stroke-width="1.3"/><path d="M6.5 13h13" stroke="#1d1e20" stroke-width="1.3"/></svg>
      <span class="line"></span>
    </div>
    <div class="contact">
      <div>044-310 872 615</div>
      <div>office@peltonmarsh.example</div>
      <div>www.peltonmarsh.example</div>
    </div>
    <div class="address-rule"></div>
    <div class="address">
      <div>87, Harwell Lane,</div>
      <div>30918,Northmere</div>
    </div>
  </section>

  <section class="card card-back">
    <div class="pattern" role="img" aria-label="Faint repeating brand pattern in dark greys"></div>
    <div class="back-brand">
      <div class="brand-square"></div>
      <div class="brand-name">Pelton|Marsh &amp; Quillan</div>
    </div>
  </section>
</main>
</body>
</html>
```